IT Freelancer (Consulting, trainer and project manager) needed letterhead

As a freelancer for IT Trainingswhip, consulting and project management I need a letterhead design. What is desired is a design that fits the existing logo (see Annex). It is functional, reliable, and equal time wirkenn Agil and modern. The whole is in color, as well as printed out to make a good impression on a black and white printer. The whole is to the existing Cooperate design (business card, homepage, logo) fit. Therefore, the choice of colors.
Updates

Target Market(s)

Customers such as medium-sized enterprises, training institutions

Industry/Entity Type

Consulting

Colors
0455a3
3277b5
85abd2
cfdfed
34a6d7
32a6d6
249fd4
0792cd
85cae6

Requirements
Must have
• Must include logo (see Annex) address (Brennerweg 14, 92660 Neustadt, Germany). Must seriously and act simultaneously Agil. Design should (even) be adaptable (signature, address, etc.) design must look good on a black / white laser

```html
<!DOCTYPE html>
<html lang="en">
<head>
<meta charset="utf-8">
<title>Konrad Falter – Letterhead</title>
<link rel="stylesheet" href="https://fonts.googleapis.com/css2?family=Source+Sans+3:wght@400;600;700&display=swap">
<style>
  :root {
    --navy: #0455a3;
    --blue-mid: #0792cd;
    --blue-bright: #1ab0ec;
    --blue-deep: #0a7fb5;
    --ink: #1d1d1d;
    --band: #474747;
    --paper: #ffffff;
    --backdrop: #e4e4e4;
  }
  html, body {
    margin: 0;
    padding: 0;
    width: 1116px;
    height: 1200px;
    overflow: hidden;
    background: var(--backdrop);
    font-family: "Source Sans 3", "Myriad Pro", Arial, sans-serif;
    color: var(--ink);
  }
  .letterhead {
    position: absolute;
    left: 109px;
    top: 21px;
    width: 801px;
    height: 1033px;
    background: var(--paper);
    transform: scale(1.12);
    transform-origin: top left;
    box-shadow: 0 2px 10px rgba(0,0,0,0.12);
    overflow: hidden;
  }
  .header-art {
    position: absolute;
    left: 0;
    top: 0;
    width: 801px;
    height: 280px;
  }
  .brand {
    position: absolute;
    left: 567px;
    top: 70px;
    width: 160px;
    text-align: center;
  }
  .brand-dot {
    display: block;
    width: 90px;
    height: 90px;
    margin: 0 auto 8px;
    border-radius: 50%;
    background: var(--navy);
  }
  .brand-name {
    margin: 0;
    font-size: 21px;
    font-weight: 700;
    line-height: 22px;
    letter-spacing: 1.5px;
    color: var(--navy);
    text-transform: uppercase;
  }
  .recipient {
    position: absolute;
    left: 106px;
    top: 289px;
  }
  .recipient-name {
    margin: 0 0 1px;
    font-size: 15px;
  }
  .recipient-line {
    margin: 0;
    font-size: 10.5px;
    line-height: 14px;
  }
  .letter-body {
    position: absolute;
    left: 106px;
    top: 379px;
    width: 621px;
  }
  .letter-body p {
    margin: 0 0 28px;
    font-size: 10.9px;
    line-height: 14px;
    text-align: justify;
    hyphens: auto;
  }
  .closing {
    position: absolute;
    left: 106px;
    top: 819px;
  }
  .closing-phrase {
    margin: 0;
    font-size: 10.5px;
  }
  .signatory {
    margin: 2px 0 0;
    font-size: 18px;
  }
  .contact-bar {
    position: absolute;
    left: 88px;
    top: 960px;
    width: 640px;
    height: 16px;
    font-size: 10.5px;
  }
  .contact-item {
    position: absolute;
    top: 0;
    display: flex;
    align-items: center;
    gap: 4px;
    white-space: nowrap;
  }
  .contact-item svg { width: 11px; height: 11px; }
  .footer-rule {
    position: absolute;
    left: 0;
    top: 988px;
    width: 801px;
    height: 4px;
    background: var(--blue-bright);
  }
  .footer-band {
    position: absolute;
    left: 0;
    top: 992px;
    width: 801px;
    height: 41px;
    background: var(--band);
  }
</style>
</head>
<body>
<main class="letterhead" lang="la">
  <svg class="header-art" viewBox="0 0 801 280" role="img" aria-label="Blue decorative header artwork in the top corner">
    <defs>
      <linearGradient id="header-fill" x1="0" y1="0" x2="1" y2="0.4">
        <stop offset="0" stop-color="var(--blue-deep)"/>
        <stop offset="0.5" stop-color="var(--blue-mid)"/>
        <stop offset="1" stop-color="var(--blue-bright)"/>
      </linearGradient>
    </defs>
    <polygon points="0,0 801,0 801,78 465,12 105,95 90,108 0,273" fill="url(#header-fill)"/>
  </svg>

  <div class="brand">
    <span class="brand-dot"></span>
    <p class="brand-name">Konrad<br>Falter</p>
  </div>

  <section class="recipient">
    <p class="recipient-name">Mr. Daniel Mercer</p>
    <p class="recipient-line">Managing Director</p>
    <p class="recipient-line">Northgate Business Center</p>
  </section>

  <section class="letter-body">
    <p>Maecenas non rutrum libero. Donec odio lorem, vehicula eu fermentum ut, varius vel purus. Sed varius faucibus enim eu tincidunt. Nullam accumsan metus elit, et blandit risus tincidunt id. Etiam laoreet ultricies est, eu venenatis orci pharetra quis. Cras ut efficitur massa. Mauris nec sodales libero, id pretium quam. Mauris et nulla nec nunc imperdiet ultricies. Sed suscipit, felis eget dignissim luctus, erat nisl euismod nibh, in dignissim nisl est et neque. Proin bibendum quis felis id dignissim. Nulla vitae elementum neque. Nam sollicitudin felis dui, quis consectetur elit accumsan a. Maecenas eget erat eleifend, fermentum metus vel, mattis nunc. Duis at rutrum ligula, sit amet finibus arcu. Aliquam lacus nulla, molestie id porta gravida, rutrum molestie nisi. Proin volutpat nisl ac pharetra dictum. Curabitur sed quam ex. Ut pellentesque pulvinar purus, at sagittis arcu porttitor eu. Nam suscipit vestibulum blandit. Ut tempus ante sed arcu sollicitudin, non hendrerit sem porttitor. In congue in justo ut vehicula. Sed pellentesque felis ut velit placerat, ut tristique massa vestibulum. Integer viverra, massa eget scelerisque tempus, magna quam convallis nibh, vel consectetur turpis diam vitae nisl. Donec lobortis placerat dolor.</p>
    <p>Nullam accumsan metus elit, et blandit risus tincidunt id. Etiam laoreet ultricies est, eu venenatis orci pharetra quis. Cras ut efficitur massa. Mauris nec sodales libero, id pretium quam. Mauris et nulla nec nunc imperdiet ultricies. Sed suscipit, felis eget dignissim luctus, erat nisl euismod nibh, in dignissim nisl est et neque. Proin bibendum quis felis id dignissim. Nulla vitae elementum neque. Nam sollicitudin felis dui, quis consectetur elit accumsan a. Maecenas eget erat eleifend, fermentum metus vel, mattis nunc. Duis at rutrum ligula, sit amet finibus arcu. Aliquam lacus nulla, molestie id porta gravida, rutrum molestie nisi. Proin volutpat nisl ac pharetra dictum. Curabitur sed quam ex accumsan eget erat.</p>
    <p>Nullam accumsan metus elit, et blandit risus tincidunt id. Etiam laoreet ultricies est, eu venenatis orci pharetra quis. Cras ut efficitur massa. Mauris nec sodales libero, id pretium quam. Mauris et nulla nec nunc imperdiet ultricies. Sed suscipit, felis eget dignissim luctus, erat nisl euismod nibh, in dignissim nisl est et neque. Proin bibendum quis felis id dignissim. Nulla vitae elementum neque. Nam sollicitudin felis dui, quis consectetur elit accumsan.</p>
  </section>

  <section class="closing" lang="en">
    <p class="closing-phrase">Sincerely</p>
    <p class="signatory">Tobias Lindqvist</p>
  </section>

  <footer class="contact-bar" lang="en">
    <span class="contact-item" style="left:0">
      <svg viewBox="0 0 12 12" aria-hidden="true"><circle cx="6" cy="6" r="5.5" fill="none" stroke="var(--blue-mid)"/><path d="M4 3.2c-.6.4-.8 1.2-.3 2.3.6 1.4 1.8 2.7 3 3.3.9.4 1.6.2 2-.3L7.6 7.3 6.9 7.8c-.6-.3-1.3-1-1.6-1.7l.5-.7z" fill="var(--blue-mid)"/></svg>
      88-321-457890
    </span>
    <span class="contact-item" style="left:133px">
      <svg viewBox="0 0 12 12" aria-hidden="true"><circle cx="6" cy="6" r="6" fill="var(--blue-mid)"/><rect x="3" y="4" width="6" height="4" fill="#fff"/><path d="M3 4l3 2.2L9 4" fill="none" stroke="var(--blue-mid)" stroke-width=".8"/></svg>
      office@falter-it.com
    </span>
    <span class="contact-item" style="left:287px">
      <svg viewBox="0 0 12 12" aria-hidden="true"><g fill="none" stroke="var(--blue-mid)" stroke-width=".9"><circle cx="6" cy="6" r="5.2"/><ellipse cx="6" cy="6" rx="2.2" ry="5.2"/><path d="M.8 6h10.4M1.8 3.4h8.4M1.8 8.6h8.4"/></g></svg>
      www.falter-it.com
    </span>
    <span class="contact-item" style="left:419px">
      <svg viewBox="0 0 12 12" aria-hidden="true"><circle cx="6" cy="6" r="6" fill="var(--blue-mid)"/><path d="M3 6.2L6 3.4l3 2.8V9H3z" fill="#fff"/></svg>
      Brennerweg 14, 92660 Neustadt, Germany
    </span>
  </footer>

  <div class="footer-rule"></div>
  <div class="footer-band"></div>
</main>
</body>
</html>
```